Business Card Design Project 4 Construction Business

I am after a creative, but sleek and simple/ clean business card design. This design will form the basis of future items and might include a logo or simply a creative way to lay out the text of my company name 'kestrel ventures'
I like the simplicity of black and white however I would also be happy to see a splash of colour introduced somehow to give the text some interest and make it stand out.
I would like a double sided card.
I am young (ish!) and professional, offering construction and project management services, what I don't want is the traditional builders type card featuring a cheesy hammer/ saw image etc.
As the company name, kestrel ventures, suggests, we focus on working closely and collaboratively together, in synergy with all stakeholders involved in the projects that we undertake
Construction

```html
<!DOCTYPE html>
<html lang="en">
<head>
<meta charset="utf-8">
<title>Kestrel Ventures – Business Card</title>
<link href="https://fonts.googleapis.com/css2?family=Montserrat:wght@400&family=Michroma&family=Arimo:wght@400&display=swap" rel="stylesheet">
<style>
  :root {
    --page-bg: #d9d9d9;
    --front-light: #f2f2f2;
    --front-mid: #a9a9a9;
    --front-dark: #3a3a3a;
    --back-top: #4a4a4a;
    --back-bottom: #232323;
    --band: #1c1c1c;
    --logo-front: #5c5c5c;
    --logo-back: #2e2e2e;
    --text-light: #d6d6d6;
    --text-muted: #b0b0b0;
    --icon-bg: #bdbdbd;
    --icon-fg: #333333;
  }
  * { box-sizing: border-box; margin: 0; padding: 0; }
  html, body {
    width: 1200px; height: 1000px; overflow: hidden;
    background: var(--page-bg);
  }
  .sheet {
    position: relative; width: 1200px; height: 1000px;
  }
  .card {
    position: absolute; left: 240px; width: 720px; height: 410px;
    overflow: hidden;
  }
  /* Front side */
  .card--front {
    top: 50px;
    background:
      radial-gradient(ellipse 70% 55% at 55% 28%, var(--front-light) 0%, rgba(242,242,242,0) 70%),
      linear-gradient(180deg, #cfcfcf 0%, var(--front-mid) 45%, var(--front-dark) 100%);
  }
  .logo {
    position: absolute; text-transform: uppercase;
    font-family: "Montserrat", sans-serif; font-weight: 400;
    text-align: center;
  }
  .card--front .logo {
    left: 0; right: 0; top: 128px; color: var(--logo-front);
  }
  .logo__main { display: block; font-size: 58px; letter-spacing: 3px; line-height: 1; }
  .logo__sub { display: block; font-size: 22px; letter-spacing: 22px; margin-top: 10px; padding-left: 22px; }
  .front-web {
    position: absolute; left: 0; right: 0; bottom: 40px; text-align: center;
    font-family: "Arimo", sans-serif; font-size: 17px; color: #2a2a2a;
  }
  /* Back side */
  .card--back {
    top: 540px;
    background: linear-gradient(160deg, var(--back-top) 0%, #363636 50%, var(--back-bottom) 100%);
  }
  .card--back .logo {
    right: 36px; top: 44px; color: var(--logo-back); text-align: center;
  }
  .card--back .logo__main { font-size: 40px; letter-spacing: 2px; }
  .card--back .logo__sub { font-size: 16px; letter-spacing: 15px; margin-top: 6px; padding-left: 15px; }
  .holder { position: absolute; left: 36px; top: 34px; }
  .holder__name {
    font-family: "Michroma", sans-serif; font-size: 24px; letter-spacing: 1px;
    color: var(--text-light); text-transform: uppercase;
  }
  .holder__role {
    font-family: "Michroma", sans-serif; font-size: 13px; letter-spacing: 2px;
    color: var(--text-muted); text-transform: uppercase; margin-top: 2px;
  }
  .contacts { position: absolute; left: 36px; top: 148px; list-style: none; }
  .contacts li {
    display: flex; align-items: center; gap: 14px; height: 38px;
    font-family: "Arimo", sans-serif; font-size: 16px; color: var(--text-light);
  }
  .contacts svg { width: 26px; height: 26px; flex: none; }
  .address-band {
    position: absolute; left: 0; right: 0; bottom: 0; height: 78px;
    background: linear-gradient(180deg, #2a2a2a, var(--band));
    display: flex; align-items: center; padding-left: 36px;
    font-family: "Arimo", sans-serif; font-size: 16px; letter-spacing: 4px;
    color: var(--text-muted);
  }
</style>
</head>
<body>
<main class="sheet">
  <section class="card card--front" aria-label="Card front">
    <div class="logo">
      <span class="logo__main">Kestrel</span>
      <span class="logo__sub">Ventures</span>
    </div>
    <p class="front-web">www.kestrelventuresgroup.com.au</p>
  </section>

  <section class="card card--back" aria-label="Card back">
    <div class="holder">
      <p class="holder__name">Liam Porter</p>
      <p class="holder__role">Director</p>
    </div>
    <div class="logo">
      <span class="logo__main">Kestrel</span>
      <span class="logo__sub">Ventures</span>
    </div>
    <ul class="contacts">
      <li>
        <svg viewBox="0 0 26 26" aria-hidden="true">
          <rect width="26" height="26" rx="3" fill="var(--icon-bg)"/>
          <path d="M9 6h3l1 4-2 1c1 2 2 3 4 4l1-2 4 1v3c0 1-1 2-2 2C12 19 7 14 7 8c0-1 1-2 2-2z" fill="var(--icon-fg)"/>
        </svg>
        <span>0400 555 000</span>
      </li>
      <li>
        <svg viewBox="0 0 26 26" aria-hidden="true">
          <rect width="26" height="26" rx="3" fill="var(--icon-bg)"/>
          <text x="13" y="19" text-anchor="middle" font-family="Arimo, sans-serif" font-size="18" fill="var(--icon-fg)">@</text>
        </svg>
        <span>liam@kestrelventuresgroup.com.au</span>
      </li>
      <li>
        <svg viewBox="0 0 26 26" aria-hidden="true">
          <rect width="26" height="26" rx="3" fill="var(--icon-bg)"/>
          <g fill="none" stroke="var(--icon-fg)" stroke-width="1.4">
            <circle cx="13" cy="13" r="8"/>
            <ellipse cx="13" cy="13" rx="3.5" ry="8"/>
            <path d="M5 13h16M6.5 9h13M6.5 17h13"/>
          </g>
        </svg>
        <span>www.kestrelventuresgroup.com.au</span>
      </li>
    </ul>
    <p class="address-band">Address. 14 Harbour Lane Ashford NSW 2000</p>
  </section>
</main>
</body>
</html>
```